Tidewell building company Business card design

I need a business card design for my company. I have a logo but dont have business cards with our logo..

www.tidewellbuildingco.com.au

The logo is on the website

I need the same details as this design I have attached. we have changed the logo and colours. just like the website

```html
<!DOCTYPE html>
<html lang="en">
<head>
<meta charset="utf-8">
<title>Tidewell Building – Business Card</title>
<link href="https://fonts.googleapis.com/css2?family=Cinzel:wght@400;700&family=Open+Sans:wght@400;600&display=swap" rel="stylesheet">
<style>
  :root {
    --page-bg: #b9bbbd;
    --card-frame: #1f7bbd;
    --card-face: #f4f5f6;
    --card-face-shade: #e3e5e7;
    --logo-panel: #fafafa;
    --name-band: #1b1b1b;
    --brand-blue: #1f7bbd;
    --ink: #1a1a1a;
    --muted: #8a8a8a;
  }
  * { box-sizing: border-box; margin: 0; padding: 0; }
  html, body { width: 1200px; height: 1000px; overflow: hidden; }
  body {
    background: radial-gradient(ellipse at 50% 40%, #d3d5d7 0%, var(--page-bg) 100%);
    font-family: "Open Sans", Arial, sans-serif;
    position: relative;
  }
  .business-card {
    position: absolute;
    left: 150px; top: 230px;
    width: 900px; height: 540px;
    border-radius: 44px;
    background: var(--card-frame);
    padding: 20px;
    box-shadow: 0 18px 40px rgba(0,0,0,0.25);
  }
  .card-face {
    position: relative;
    width: 100%; height: 100%;
    border-radius: 28px;
    background: linear-gradient(135deg, var(--card-face) 0%, var(--card-face-shade) 100%);
    overflow: hidden;
  }
  .logo-panel {
    position: absolute;
    left: 60px; top: 40px;
    width: 340px; height: 340px;
    background: var(--logo-panel);
    display: flex; flex-direction: column;
    align-items: center; justify-content: center;
    gap: 22px;
  }
  .brand-square {
    width: 90px; height: 90px;
    background: var(--brand-blue);
  }
  .brand-name {
    font-family: "Cinzel", Georgia, serif;
    font-weight: 700;
    color: var(--brand-blue);
    font-size: 44px;
    line-height: 1.05;
    text-align: center;
    letter-spacing: 2px;
  }
  .name-band {
    position: absolute;
    right: 0; top: 34px;
    width: 430px; height: 100px;
    background: var(--name-band);
    padding: 20px 30px 0 40px;
  }
  .person-name {
    font-family: "Cinzel", Georgia, serif;
    font-weight: 400;
    color: var(--brand-blue);
    font-size: 28px;
    line-height: 36px;
    letter-spacing: 1px;
    white-space: nowrap;
  }
  .person-role {
    font-family: "Cinzel", Georgia, serif;
    color: var(--muted);
    font-weight: 700;
    font-size: 16px;
    line-height: 20px;
    text-align: right;
    margin-top: 2px;
  }
  .contact-list {
    position: absolute;
    left: 440px; top: 180px;
    list-style: none;
  }
  .contact-item {
    display: flex; align-items: center;
    gap: 20px;
    height: 52px;
    font-size: 17px;
    color: var(--ink);
    white-space: nowrap;
  }
  .contact-icon { width: 32px; height: 32px; flex: none; }
  .postal-address {
    position: absolute;
    left: 140px; bottom: 46px;
    display: flex; align-items: center; gap: 22px;
    font-size: 23px;
    letter-spacing: 1px;
    color: var(--ink);
    font-style: normal;
    white-space: nowrap;
  }
  .postal-address .contact-icon { width: 40px; height: 40px; }
</style>
</head>
<body>
  <section class="business-card" aria-label="Tidewell Building business card">
    <div class="card-face">
      <div class="logo-panel">
        <span class="brand-square" aria-hidden="true"></span>
        <p class="brand-name">TIDEWELL<br>BUILDING</p>
      </div>

      <header class="name-band">
        <h1 class="person-name">MAREK DOBRESCU</h1>
        <p class="person-role">Director</p>
      </header>

      <ul class="contact-list">
        <li class="contact-item">
          <svg class="contact-icon" viewBox="0 0 34 34" aria-hidden="true">
            <rect x="4" y="9" width="26" height="20" rx="3" fill="var(--brand-blue)"/>
            <rect x="8" y="4" width="18" height="8" rx="3" fill="var(--brand-blue)"/>
            <g fill="#fff"><rect x="9" y="15" width="3" height="3"/><rect x="15" y="15" width="3" height="3"/><rect x="21" y="15" width="3" height="3"/><rect x="9" y="21" width="3" height="3"/><rect x="15" y="21" width="3" height="3"/><rect x="21" y="21" width="3" height="3"/></g>
          </svg>
          <span>9412 5730</span>
        </li>
        <li class="contact-item">
          <svg class="contact-icon" viewBox="0 0 34 34" aria-hidden="true">
            <rect x="9" y="2" width="16" height="30" rx="3" fill="none" stroke="var(--brand-blue)" stroke-width="2.5"/>
            <circle cx="17" cy="28" r="1.6" fill="var(--brand-blue)"/>
          </svg>
          <span>0412558093</span>
        </li>
        <li class="contact-item">
          <svg class="contact-icon" viewBox="0 0 34 34" aria-hidden="true">
            <rect x="2" y="8" width="30" height="20" fill="var(--brand-blue)"/>
            <path d="M2 8 L17 20 L32 8" fill="none" stroke="#fff" stroke-width="2"/>
          </svg>
          <span>info@tidewellbuildingco.com.au/</span>
        </li>
        <li class="contact-item">
          <svg class="contact-icon" viewBox="0 0 34 34" aria-hidden="true">
            <g fill="none" stroke="var(--brand-blue)" stroke-width="2">
              <circle cx="17" cy="17" r="14"/>
              <ellipse cx="17" cy="17" rx="6" ry="14"/>
              <line x1="3" y1="17" x2="31" y2="17"/>
              <path d="M6 9 H28 M6 25 H28"/>
            </g>
          </svg>
          <span>http://www.tidewellbuildingco.com.au/</span>
        </li>
      </ul>

      <address class="postal-address">
        <svg class="contact-icon" viewBox="0 0 40 40" aria-hidden="true">
          <rect x="3" y="14" width="30" height="24" rx="4" fill="none" stroke="var(--brand-blue)" stroke-width="2.5"/>
          <path d="M22 2 a8 8 0 0 1 8 8 c0 6 -8 14 -8 14 s-8 -8 -8 -14 a8 8 0 0 1 8 -8z" fill="var(--brand-blue)"/>
          <circle cx="22" cy="10" r="3" fill="#fff"/>
        </svg>
        <span>Unit 1 Level 1,27 Marlow Ave,Kestrel Bay,WA 6031</span>
      </address>
    </div>
  </section>
</body>
</html>
```